QM active wear

Hey There

QM is a brand new active wear Sydney base company. our clothe design by professional dancers & athletics. pushing the niche market of active wear. the products we have is cool fashionable functional Eco friendly!!!

it caters male and female. who stays active and wants to be chic at the same time.
we would like to be associate with K-8 & Coastal garments & Vorn kind of brands.

i need you guys to use the existing logo to restructure it. turn it into consistent format that can be shared through out all the electronic business stationery. pls refer to all the photos i have upload in this brief. hopefully it'll gives you guys more of what i like i needs to be done.

PS: business card material specifications needs to be provided.
just so send the details to the printing company without explain too much.

Cheers

Industry/Entity Type

Electronic

Requirements
Must have
• It needs be more readable. clean. current. pop. fashionable.
interesting details across the broad for all electronic stationary.

for you to think about it and working on : company's business letters, order forms, its notices and other official publications, promissory notes, endorsements, cheques and orders for money or goods purporting to be signed by, or on behalf of, the company invoices, receipts websites

```html
<!DOCTYPE html>
<html lang="en">
<head>
<meta charset="utf-8">
<title>QM active wear – Business Card</title>
<link rel="stylesheet" href="https://fonts.googleapis.com/css2?family=Open+Sans:wght@400;600&display=swap">
<style>
  :root {
    --backdrop: #5b5b5d;
    --teal: #26a196;
    --teal-light: #3cc2b4;
    --card-black: #1c1c1d;
    --ink-dark: #2a2d2e;
    --text-light: #d4d6d6;
    --text-muted: #8a8e8e;
    --shadow: rgba(0, 0, 0, 0.45);
  }
  * { box-sizing: border-box; margin: 0; padding: 0; }
  html, body {
    width: 1200px;
    height: 716px;
    overflow: hidden;
    background: var(--backdrop);
    font-family: "Open Sans", Arial, sans-serif;
  }
  .stage {
    position: relative;
    width: 1200px;
    height: 716px;
    display: flex;
    align-items: center;
    justify-content: center;
    gap: 60px;
  }
  .card {
    position: relative;
    width: 500px;
    height: 286px;
    border-radius: 3px;
    box-shadow: 0 14px 30px var(--shadow);
  }
  /* Front side */
  .card-front {
    background: var(--teal);
    display: flex;
    align-items: center;
    justify-content: center;
    gap: 26px;
  }
  .card-front .brand-disc {
    width: 170px;
    height: 170px;
    border-radius: 50%;
    background: var(--ink-dark);
    flex: none;
  }
  .card-front .brand-name {
    font-size: 26px;
    font-weight: 600;
    line-height: 1.15;
    color: var(--ink-dark);
    letter-spacing: 1px;
  }
  /* Back side */
  .card-back {
    background: var(--card-black);
  }
  .brand-block {
    position: absolute;
    left: 34px;
    top: 96px;
    width: 190px;
    text-align: center;
  }
  .brand-block .brand-name {
    font-size: 30px;
    font-weight: 600;
    line-height: 1.1;
    color: var(--teal-light);
    letter-spacing: 1px;
  }
  .brand-block .tagline {
    margin-top: 6px;
    font-size: 8px;
    letter-spacing: 1.5px;
    color: var(--text-muted);
    text-transform: uppercase;
  }
  .contact-list {
    position: absolute;
    left: 268px;
    top: 92px;
    list-style: none;
    font-size: 12px;
    line-height: 20px;
    color: var(--text-light);
    white-space: nowrap;
  }
  .contact-list li {
    display: flex;
    align-items: flex-start;
    gap: 10px;
  }
  .contact-list .icon {
    width: 12px;
    height: 12px;
    margin-top: 4px;
    flex: none;
    fill: var(--text-light);
  }
  .contact-list .no-icon { width: 12px; flex: none; }
</style>
</head>
<body>
  <main class="stage">
    <section class="card card-front" aria-label="Business card front">
      <span class="brand-disc" aria-hidden="true"></span>
      <span class="brand-name">QM<br>active wear</span>
    </section>

    <section class="card card-back" aria-label="Business card back">
      <div class="brand-block">
        <div class="brand-name">QM<br>active wear</div>
        <div class="tagline">Move free, just move</div>
      </div>

      <ul class="contact-list">
        <li>
          <svg class="icon" viewBox="0 0 12 12" aria-hidden="true"><circle cx="6" cy="4" r="3.5"/><rect x="5.2" y="6" width="1.6" height="6"/></svg>
          <span>Harbour Lane 214</span>
        </li>
        <li><span class="no-icon"></span><span>Surry Hills, NSW 2010</span></li>
        <li>
          <svg class="icon" viewBox="0 0 12 12" aria-hidden="true"><path d="M3 0h6a1 1 0 0 1 1 1v10a1 1 0 0 1-1 1H3a1 1 0 0 1-1-1V1a1 1 0 0 1 1-1zm0 2v7h6V2z"/></svg>
          <span>+61 2 9555 0148</span>
        </li>
        <li>
          <svg class="icon" viewBox="0 0 12 12" aria-hidden="true"><path d="M0 2h12v1L6 7 0 3z"/><path d="M0 4.5l6 4 6-4V10H0z"/></svg>
          <span>alexreed@mail.com</span>
        </li>
        <li>
          <svg class="icon" viewBox="0 0 12 12" aria-hidden="true"><path d="M6 0l6 5.5h-2V11H7.5V7.5h-3V11H2V5.5H0z"/></svg>
          <span>http://www.qmactivewear.com</span>
        </li>
      </ul>
    </section>
  </main>
</body>
</html>
```